TRU PEAK POWER.

I'd like my business logo.
contact name: Desmond Halvik
phone:0438275160
email: info@trupeakpower.net.au
website: www.trupeakpower.net.au

services:
solar
battery storage
LED lighting
energy saving solutions
general electrical
I'd like the design to look professional

Target Market(s)

Everyone

Industry/Entity Type

Business

Contact Information for Business Card

as described above

Requirements
Must have
• Id like the colours and the design to work well with my logo.

```html
<!DOCTYPE html>
<html lang="en">
<head>
<meta charset="utf-8">
<title>Tru Peak Power – Business Card</title>
<link rel="stylesheet" href="https://fonts.googleapis.com/css2?family=Open+Sans:wght@400;600;700&display=swap">
<style>
  :root {
    --stage: #000000;
    --card-light: #f3f3f3;
    --ink: #222222;
    --accent-orange: #e8901a;
    --brand-green: #5aab3a;
    --green-light: #8cc63f;
    --green-deep: #5aa934;
    --white: #ffffff;
  }
  * { margin: 0; padding: 0; box-sizing: border-box; }
  html, body { width: 1200px; height: 900px; overflow: hidden; background: var(--stage); }
  body { font-family: "Open Sans", Arial, sans-serif; position: relative; }

  .card { position: absolute; top: 200px; width: 310px; height: 502px; }
  .card-front {
    left: 265px; background: var(--card-light);
    border-radius: 58px 0 58px 0;
  }
  .card-back {
    left: 641px; width: 309px;
    border-radius: 0 58px 0 58px;
    background: radial-gradient(circle at 55% 35%, var(--green-light) 0%, #7cbd3b 45%, var(--green-deep) 100%);
    color: var(--white);
  }

  .brand-mark {
    position: absolute; left: 50%; top: 60px; transform: translateX(-50%);
    width: 62px; height: 62px; border-radius: 50%; background: var(--accent-orange);
  }
  .brand-name {
    position: absolute; left: 0; width: 100%; text-align: center;
    font-weight: 700; line-height: 1.05; letter-spacing: -0.5px;
  }
  .card-front .brand-name { top: 168px; font-size: 36px; color: var(--brand-green); }
  .card-back .brand-name { top: 70px; font-size: 38px; color: var(--white); }

  .contact-name {
    position: absolute; left: 27px; top: 362px;
    font-size: 18px; font-weight: 600; color: var(--accent-orange);
  }
  .contact-list { position: absolute; left: 27px; top: 410px; list-style: none; }
  .contact-list li {
    display: flex; align-items: center; height: 21px;
    font-size: 13px; color: var(--ink);
  }
  .contact-list svg { width: 10px; height: 10px; margin-right: 8px; fill: var(--accent-orange); }

  .services-title {
    position: absolute; left: 32px; top: 298px;
    font-size: 27px; font-weight: 600;
  }
  .service-list { position: absolute; left: 32px; top: 348px; list-style: none; }
  .service-list li {
    display: flex; align-items: center; height: 23.5px;
    font-size: 15px; font-weight: 600;
  }
  .service-list li::before {
    content: ""; width: 11px; height: 11px; border-radius: 50%;
    background: var(--white); margin-right: 12px;
  }
</style>
</head>
<body>
  <section class="card card-front">
    <div class="brand-mark"></div>
    <div class="brand-name">TRU PEAK<br>POWER</div>
    <div class="contact-name">Desmond Halvik</div>
    <ul class="contact-list">
      <li><svg viewBox="0 0 10 10"><path d="M2 0.5l2 2-1 1.2c.6 1.3 1.7 2.4 3 3l1.2-1 2 2-1.2 1.8C4.5 9.2.8 5.5.3 1.7z"/></svg>0438275160</li>
      <li><svg viewBox="0 0 10 10"><path d="M0 2h10v6H0z M0 2l5 3.3L10 2" stroke="#f3f3f3" stroke-width="0.8"/></svg>info@trupeakpower.net.au</li>
      <li><svg viewBox="0 0 10 10"><circle cx="5" cy="5" r="5"/></svg>www.trupeakpower.net.au</li>
    </ul>
  </section>

  <section class="card card-back">
    <div class="brand-name">TRU PEAK<br>POWER</div>
    <h2 class="services-title">What I do</h2>
    <ul class="service-list">
      <li>Solar</li>
      <li>Battery Storage</li>
      <li>LED Lighting</li>
      <li>Energy Saving Solutions</li>
    </ul>
  </section>
</body>
</html>
```